New Look Driving School Project

Current website:
www. pelmarsteeracademy.com

Websites that we like (use content and courses from here as well):
https://www. quorbeltlessons.com

We are looking for a fresh looking driving school website that is easy for students to find the course they are looking for, the price, and allow them to book a lesson all on our website. We would like for this website to have multiple pages: Home, Teen Courses, Adult Courses, About Us, Contact, FAQ, Blog, Requirements.

Target Market(s)

Students in High School or Parents

Industry/Entity Type

Education

Coding

Coded - Design and coding required

Number of Pages Required

5+ page

Font styles to use
Serif
Sans Serif

Colors

Designer to choose colors to be used in the design.

Requirements
Must have
• Must have a form submission and payment processing option. Must have the ability to pick a course, see available times, and process their payment online. MUST BE MOBILE FRIENDLY DESIGN.
Nice to have
• Nice to have a clean format, with big bold fonts.
Should not have
• Should not have a lot of sliders or animations. Should be very fast loading on mobile. Keep it simple but easy to read and elegant.

```html
<!DOCTYPE html>
<html lang="en">
<head>
<meta charset="utf-8">
<title>Pelmar Steer – Driving Lessons</title>
<link href="https://fonts.googleapis.com/css2?family=Lato:wght@300;400;700;900&family=Dancing+Script:wght@500&display=swap" rel="stylesheet">
<style>
:root{
  --brand-purple:#2a0a5a;
  --brand-teal:#0a6a8a;
  --accent-blue:#1d8fc6;
  --gold:#d7d300;
  --ink:#111;
  --muted:#999;
  --panel:#f5f5f5;
  --white:#fff;
  --line-teal:#1aa3c8;
}
*{box-sizing:border-box;margin:0;padding:0}
html,body{width:1200px;height:2807px;overflow:hidden}
body{font-family:'Lato',sans-serif;color:var(--ink);background:var(--white);position:relative}
.abs{position:absolute}
.script{font-family:'Dancing Script',cursive;color:var(--accent-blue)}

/* header */
.top-bar{left:0;top:0;width:1200px;height:101px;background:linear-gradient(90deg,var(--brand-purple),var(--brand-teal))}
.top-btn{left:8px;width:100px;height:26px;background:#1b1450;color:#fff;font-size:10px;font-weight:700;display:flex;align-items:center;justify-content:center;border-radius:2px}
.brand{left:0;width:1200px;top:26px;text-align:center;color:#fff;font-size:30px;font-weight:900;letter-spacing:1px}
.contact-line{right:70px;text-align:right;color:#fff;font-size:11px;font-weight:700}
.contact-line small{display:block;font-size:8px;font-weight:400;color:var(--line-teal)}
.contact-icon{right:34px}
.main-nav{left:0;top:101px;width:1200px;height:39px;background:#000;border-bottom:2px solid var(--line-teal);display:flex;justify-content:center;gap:40px;align-items:center}
.main-nav a{color:var(--line-teal);font-size:10px;text-decoration:none;text-transform:uppercase}

/* hero */
.hero-photo{left:0;top:140px;width:1200px;height:458px;background:linear-gradient(100deg,#6b6b78 0%,#b9c2d2 40%,#d9c7bb 70%,#8a7a70 100%)}
.lead-form{left:45px;top:184px;width:363px;height:314px;background:linear-gradient(135deg,rgba(42,10,90,.93),rgba(10,106,138,.93));border:2px solid var(--line-teal);padding:12px 13px}
.lead-form h2{color:#fff;font-size:20px;font-weight:700;margin-bottom:6px}
.field label{display:block;color:#aaa;font-size:9px;margin-bottom:2px}
.field span{display:block;height:23px;background:#fff;margin-bottom:6px}
.pair{display:flex;gap:8px}.pair .field{flex:1}
.send{height:25px;background:#0b1a5a;color:#fff;font-size:10px;display:flex;align-items:center;justify-content:center;margin-top:2px}

/* packages */
.section-title{left:0;width:1200px;text-align:center;font-size:40px;font-weight:400}
.packages-sub{left:0;top:742px;width:1200px;text-align:center;font-size:10px;color:var(--muted)}
.plan{top:802px;width:240px;height:350px;background:var(--panel);text-align:center}
.plan h3{font-size:21px;font-weight:400;margin-top:18px}
.price{font-size:56px;font-weight:900;color:var(--accent-blue);margin-top:28px}
.price sup{font-size:18px;vertical-align:top;position:relative;top:10px}
.plan ul{list-style:none;margin-top:20px;font-size:11px;color:var(--accent-blue)}
.plan li{height:27px}
.plan .cta{display:inline-block;width:116px;height:30px;border:2px solid #111;font-size:8px;font-weight:900;line-height:26px;margin-top:8px}
.plan-gold{left:480px;top:796px;height:368px;background:#fff;box-shadow:0 0 8px rgba(0,0,0,.35);z-index:2}
.plan-gold h3,.plan-gold .price{color:var(--gold)}
.plan-gold ul{color:#111;font-size:10px;margin:18px 55px 0}
.plan-gold li{height:33px;line-height:33px;border-bottom:2px solid var(--gold)}
.plan-gold .cta{background:var(--gold);margin-top:8px}
.ribbon{left:0;top:0;width:60px;height:60px;overflow:hidden}
.ribbon span{position:absolute;left:-24px;top:16px;width:100px;background:#000;color:#fff;font-size:7px;transform:rotate(-45deg);text-align:center;padding:2px 0}

/* stats */
.road-photo{left:0;top:1227px;width:1200px;height:226px;background:linear-gradient(180deg,#6f6b5a 0%,#6c6c6c 30%,#8a8a86 70%,#5f5c55 100%)}
.stat{top:1300px;width:200px;text-align:center;color:#fff}
.stat b{display:block;font-size:44px;font-weight:400}
.stat span{font-size:12px}

/* features */
.feature{width:330px;text-align:center}
.feature h4{font-size:16px;font-weight:400;margin:6px 0 8px}
.feature p{font-size:9px;color:#aaa;line-height:14px}

/* learning + faq */
.city-photo{left:0;top:1890px;width:1200px;height:418px;background:linear-gradient(90deg,#8e9aa3,#c9cdd0 60%,#a7a9ab)}
.sign-art{left:88px;top:1890px;width:666px;height:387px;background:#35876d;border:6px solid #fff;border-top:none;border-radius:0 0 10px 10px}
.faq-title{left:756px;top:1955px;width:380px;text-align:center}
.faq-title h2{font-size:26px;font-weight:700}
.faq-title p{font-size:12px}
.faq-item{left:756px;width:384px;height:48px;background:#fff;box-shadow:0 2px 6px rgba(0,0,0,.25);display:flex;align-items:center;justify-content:space-between;padding:0 18px;font-size:10px;font-weight:900;text-transform:uppercase}

/* testimonials */
.quote{top:2447px;width:350px;height:145px;background:#fff;box-shadow:0 0 8px rgba(0,0,0,.12);padding:28px 22px;font-size:10px;line-height:18px}
.person{display:flex;align-items:center;gap:10px;margin-top:12px}
.avatar{width:32px;height:32px;border-radius:50%;background:#8b8f93}
.person b{display:block;font-size:12px}
.person small{font-size:9px;color:#aaa}

/* footer */
.site-footer{left:0;top:2655px;width:1200px;height:152px;background:linear-gradient(90deg,var(--brand-purple),var(--brand-teal))}
.foot-brand{left:260px;top:2708px;color:#fff;font-size:26px;font-weight:900}
.foot-nav{left:444px;top:2697px;display:flex;gap:20px;font-size:9px;color:var(--line-teal)}
.foot-phone{left:874px;top:2697px;color:#fff;font-size:9px;font-weight:700}
.foot-rule{left:438px;top:2740px;width:516px;height:1px;background:rgba(255,255,255,.25)}
.foot-copy{left:444px;top:2766px;font-size:7px;color:#4a6a8a}
.social{left:874px;top:2766px;display:flex;gap:13px}
.social i{width:8px;height:8px;border-radius:50%;background:#fff;display:block}
</style>
</head>
<body>

<header>
  <div class="abs top-bar"></div>
  <div class="abs top-btn" style="top:12px">Register Online</div>
  <div class="abs top-btn" style="top:49px">Driving Packages</div>
  <div class="abs brand">Pelmar Steer</div>
  <div class="abs contact-line" style="top:16px">Mon - Fri: 9:00 - 17:30<small>Online store always open</small></div>
  <svg class="abs contact-icon" style="top:16px" width="26" height="26" viewBox="0 0 26 26"><circle cx="13" cy="13" r="11" fill="none" stroke="#ccc" stroke-width="2"/><path d="M13 7v6l4 2" stroke="#ccc" stroke-width="2" fill="none"/></svg>
  <div class="abs contact-line" style="top:60px">+34 700 555 0142<small>24/7 Customer Support</small></div>
  <svg class="abs contact-icon" style="top:58px" width="26" height="26" viewBox="0 0 26 26"><path d="M6 3l5 5-3 3c2 4 4 6 7 7l3-3 5 5-3 3C11 23 3 15 3 6z" fill="#ccc"/></svg>
  <nav class="abs main-nav">
    <a>Teen Courses</a><a>Adult Courses</a><a>About Us</a><a>Contact Us</a><a>Blog</a><a>Requirements</a>
  </nav>
</header>

<section>
  <div class="abs hero-photo" role="img" aria-label="Photo of a smiling student driver and instructor in a car"></div>
  <form class="abs lead-form">
    <h2>Find a Driving Instructor Today</h2>
    <div class="field"><label>Name</label><span></span></div>
    <div class="field"><label>Email</label><span></span></div>
    <div class="field"><label>Phone</label><span></span></div>
    <div class="pair"><div class="field"><label>Car Type</label><span></span></div><div class="field"><label>Licence Type</label><span></span></div></div>
    <div class="pair"><div class="field"><label>Date</label><span></span></div><div class="field"><label>Time</label><span></span></div></div>
    <div class="send">Send</div>
  </form>
</section>

<section>
  <h2 class="abs section-title" style="top:656px">Packages</h2>
  <div class="abs script" style="left:577px;top:690px;font-size:30px">To Suit You</div>
  <p class="abs packages-sub">You will be charged for the plan after the admin approves your vendor account</p>

  <div class="abs plan" style="left:240px">
    <h3>Silver</h3><div class="price"><sup>$</sup>250</div>
    <ul><li>1 x Lesson</li><li>Pre-licensing Class</li><li>Road Test Appointment</li><li>Test Car Supplied</li></ul>
    <span class="cta">GET STARTED</span>
  </div>
  <div class="abs plan plan-gold">
    <div class="abs ribbon"><span>POPULAR</span></div>
    <h3>Gold</h3><div class="price"><sup>$</sup>350</div>
    <ul><li>5 x Lessons</li><li>Pre-Licensing Class</li><li>Road Test Appointment</li><li>Test Car Supplied</li></ul>
    <span class="cta">GET STARTED</span>
  </div>
  <div class="abs plan" style="left:720px">
    <h3>Platinum</h3><div class="price"><sup>$</sup>500</div>
    <ul><li>10x Lessons</li><li>Pre-Licensing Class</li><li>Road Test Appointment</li><li>Test Car Supplied</li></ul>
    <span class="cta">GET STARTED</span>
  </div>
</section>

<section>
  <div class="abs road-photo" role="img" aria-label="Photo of an asphalt road with yellow centre lines"></div>
  <div class="abs stat" style="left:257px"><b>100%</b><span>Satisfaction Guaranteed</span></div>
  <div class="abs stat" style="left:500px"><b>20,000+</b><span>Teaching Hours</span></div>
  <div class="abs stat" style="left:743px"><b>$0</b><span>Pick-up &amp; Drop-Off</span></div>
</section>

<section>
  <div class="abs feature" style="left:255px;top:1565px">
    <svg width="24" height="38" viewBox="0 0 24 38"><text x="12" y="34" font-size="40" font-family="Lato" font-weight="900" text-anchor="middle">$</text></svg>
    <h4>AFFORDABLE</h4><p>Click edit button to change this text. Lorem ipsum dolor sit amet, consectetur adipiscing elit.</p>
  </div>
  <div class="abs feature" style="left:615px;top:1565px">
    <svg width="46" height="38" viewBox="0 0 46 38"><path d="M10 8h26l5 12v12h-6v-4H11v4H5V20z" fill="#111"/><rect x="14" y="11" width="18" height="8" fill="#fff"/><circle cx="12" cy="23" r="3" fill="#fff"/><circle cx="34" cy="23" r="3" fill="#fff"/></svg>
    <h4>EXPERIENCE</h4><p>Click edit button to change this text. Lorem ipsum dolor sit amet, consectetur adipiscing elit.</p>
  </div>
  <div class="abs feature" style="left:255px;top:1712px">
    <svg width="36" height="36" viewBox="0 0 36 36"><path d="M4 18l9 9 19-19" stroke="#111" stroke-width="6" fill="none"/></svg>
    <h4>GUARANTEE</h4><p>Click edit button to change this text. Lorem ipsum dolor sit amet, consectetur adipiscing elit.</p>
  </div>
  <div class="abs feature" style="left:615px;top:1712px">
    <svg width="36" height="36" viewBox="0 0 36 36"><polygon points="18,1 22,8 30,5 29,13 36,18 29,23 30,31 22,28 18,35 14,28 6,31 7,23 0,18 7,13 6,5 14,8" fill="#111"/></svg>
    <h4>CERTIFICATION</h4><p>Click edit button to change this text. Lorem ipsum dolor sit amet, consectetur adipiscing elit.</p>
  </div>
</section>

<section>
  <div class="abs city-photo" role="img" aria-label="Blurred photo of a city street with traffic lights"></div>
  <div class="abs sign-art" role="img" aria-label="Illustration of a green road sign with three arrows reading Learning"></div>
  <div class="abs faq-title"><h2>FAQ</h2><p>Most frequent questions and answers</p></div>
  <div class="abs faq-item" style="top:2038px">How long is road test appointment?<span>▸</span></div>
  <div class="abs faq-item" style="top:2090px">How old do I have to be to get my license?<span>▸</span></div>
  <div class="abs faq-item" style="top:2143px">What is the minimum hours required?<span>▸</span></div>
  <div class="abs faq-item" style="top:2195px">Can I chose my instructor?<span>▸</span></div>
</section>

<section>
  <h2 class="abs section-title" style="top:2368px">Hear From</h2>
  <div class="abs script" style="left:507px;top:2400px;font-size:30px">Our Successful Students</div>
  <div class="abs quote" style="left:240px">
    Click edit button to change this text. Lorem ipsum dolor sit amet, consectetur adipiscing elit. Ut elit tellus, luctus nec ullamcorper mattis, pulvinar dapibus leo.
    <div class="person"><div class="avatar" role="img" aria-label="Student portrait"></div><div><b>John Doe</b><small>Teen Student</small></div></div>
  </div>
  <div class="abs quote" style="left:610px">
    Click edit button to change this text. Lorem ipsum dolor sit amet, consectetur adipiscing elit. Ut elit tellus, luctus nec ullamcorper mattis, pulvinar dapibus leo.
    <div class="person"><div class="avatar" role="img" aria-label="Student portrait"></div><div><b>Joh Doe</b><small>Adult Student</small></div></div>
  </div>
</section>

<footer>
  <div class="abs site-footer"></div>
  <div class="abs foot-brand">Pelmar Steer</div>
  <div class="abs foot-nav"><span>Teen Courses</span><span>Adult Courses</span><span>About Us</span><span>Contact Us</span><span>Blog</span><span>Requirements</span></div>
  <div class="abs foot-phone">+1 555-010-4477</div>
  <div class="abs foot-rule"></div>
  <div class="abs foot-copy">© 2019 All rights Reserved.</div>
  <div class="abs social"><i></i><i></i><i></i><i></i></div>
</footer>

</body>
</html>
```